DJ VAZ (POSTER BANNER)

I just added a sketch to make it easier.
Also it is added:
Under the logo a tag line that says:
DJ-SERVICE-RENTALS

The information given is all is needed for the banner.
The banner needs to be horizontally rather than vertical.
The picture provided is more for a reference point rather for it to be the focal point of the banner.
The logo needs to be the focal point. Also, the phone number needs to be big but not bigger than the email address.
The vibe of the banner needs to be very energetic since I primarily do Vorlund events.

Size of banner is 4x8

Colors:
I like that deep blue, deep red, a little black.
I mainly want for it to call attention.

Need a big poster design for an event that I have coming up. I will provide with the logos that unfortunately will have to be recreated because it is in Photoshop.

I'm sending you some items that I think will be needed, but let me know if you need anything else please.

Phone: 555.014.2368
email: DJ@DJVAZ.net

Target Market(s)

Audience form 18-39
I DJ at a lot of Vorlund events and this event is one of them.

Industry/Entity Type

Events

Requirements
Must have
• Needs to be horizontal.
Red color scheme
Nice to have
• Abstract design to complement the logo the overall finish look of the banner
Should not have
• The picture MUST not be the focal point of the design.
The design should be kinda modern. If you want to use illustrations, they need to be related to Vorlund and Turntables (but needs to be limited)
I added some pictures for ideas.
I'm a little more inclined to use the logo without the slogan in it.

```html
<!DOCTYPE html>
<html lang="en">
<head>
<meta charset="utf-8">
<title>DJ VAZ — DJ Service Rentals Banner</title>
<link href="https://fonts.googleapis.com/css2?family=Orbitron:wght@900&family=Audiowide&display=swap" rel="stylesheet">
<style>
  :root {
    --ink: #050505;
    --night-blue: #1a2250;
    --deep-red: #5e120e;
    --green: #0f6a36;
    --deep-green: #0a3a22;
    --rust: #a9441c;
    --red: #8f1a10;
    --ice: #d7f3f4;
    --white: #f4f7ff;
    --logo-band: rgba(200, 120, 60, 0.5);
    --phone-blue: #3da6f0;
    --mail-blue: #2a62c9;
  }
  * { box-sizing: border-box; margin: 0; padding: 0; }
  html, body { width: 1200px; height: 600px; overflow: hidden; background: var(--ink); }
  .banner {
    position: relative;
    width: 1200px;
    height: 600px;
    overflow: hidden;
  }
  .backdrop {
    position: absolute; inset: 0;
    background: linear-gradient(90deg,
      var(--night-blue) 0%,
      var(--deep-red) 16%,
      var(--green) 30%,
      var(--deep-red) 36%,
      var(--ink) 43%,
      var(--deep-green) 52%,
      var(--ink) 60%,
      var(--rust) 76%,
      var(--red) 86%,
      var(--ink) 100%);
  }
  .logo-band {
    position: absolute; left: 240px; top: 95px; width: 700px; height: 98px;
    background: var(--logo-band);
    display: flex; align-items: center; justify-content: center;
  }
  .logo {
    font-family: "Orbitron", sans-serif; font-weight: 900;
    font-size: 96px; line-height: 1; letter-spacing: 14px;
    padding-left: 14px;
    color: var(--ink); white-space: nowrap;
  }
  .tagline {
    position: absolute; left: 0; right: 0; top: 216px; text-align: center;
    padding-left: 6px;
    font-family: "Audiowide", sans-serif; font-size: 40px; letter-spacing: 3px;
    color: var(--ice); text-transform: uppercase; white-space: nowrap;
  }
  .contact { position: absolute; left: 423px; top: 335px; }
  .contact-row { display: flex; align-items: center; gap: 18px; margin-bottom: 8px; }
  .contact-row svg { flex: none; }
  .contact-text {
    font-family: "Audiowide", sans-serif; font-size: 22px; letter-spacing: 4px;
    color: var(--white); font-style: italic; white-space: nowrap;
  }
</style>
</head>
<body>
<main class="banner">
  <div class="backdrop" role="img" aria-label="Photo collage of a DJ at turntables and performers on a lit stage over coloured bands"></div>

  <div class="logo-band">
    <h1 class="logo">DJ VAZ</h1>
  </div>
  <p class="tagline">DJ-Service-Rentals</p>

  <div class="contact">
    <div class="contact-row">
      <svg width="54" height="54" viewBox="0 0 54 54" aria-hidden="true">
        <rect x="1" y="1" width="52" height="52" rx="11" fill="var(--phone-blue)"/>
        <path d="M17 13c2-1 4 0 5 2l3 5c1 2 0 3-1 4l-2 2c1 4 5 8 9 9l2-2c1-1 2-2 4-1l5 3c2 1 3 3 2 5l-2 3c-2 2-6 2-10 0-7-4-13-10-16-17-2-4-2-8 0-10z" fill="#fff"/>
      </svg>
      <span class="contact-text">555.014.2368</span>
    </div>
    <div class="contact-row">
      <svg width="50" height="50" viewBox="0 0 50 50" aria-hidden="true">
        <circle cx="25" cy="25" r="23" fill="var(--mail-blue)" stroke="#cfe0ff" stroke-width="2"/>
        <rect x="12" y="16" width="26" height="18" rx="2" fill="#fff"/>
        <path d="M12 17l13 10 13-10" fill="none" stroke="var(--mail-blue)" stroke-width="2"/>
      </svg>
      <span class="contact-text">DJ@DJVAZ.net</span>
    </div>
  </div>
</main>
</body>
</html>
```